Posters to advertise a jewellery design school

I would like two pieces of artwork designing for our jewellery design school in Kuala Lumpur Malaysia.
60cm by 180cm poster
100cm by 100cm poster

My personal style is ‘perfectly imperfect’ but we wold like to show that we give quality classes in a fun and artistic / creative environment

The posters must contain our logo and you can choose to use as many or as few images as you like to tell the story or even include hand drawn line images.

https://files.mistreloom.net/share/folders/7kQpR2xZ9mWt4LbN__yHc8sDe3JfVa6g?usp=sharing

Please include the following wording on the poster
So you want to be a jewellery designer?

Part time and full-time classes available in:
Silversmithing
Jewellery design and rendering
Stone setting
Gemmology
Enamelling
Computer aided design
60cm by 180cm poster
100cm by 100cm poster

The posters must contain our logo and you can choose to use as many or as few images as you like to tell the story.

Silversmithing
Stone setting
Gemmology
Enamelling
Computer aided design

60cm by 180cm poster
100cm by 100cm poster

Silversmithing
Stone setting
Gemmology
Enamelling
Computer aided design

```html
<!DOCTYPE html>
<html lang="en">
<head>
<meta charset="utf-8">
<title>Mira Halden Jewellery – Roll-up Banner</title>
<link rel="stylesheet" href="https://fonts.googleapis.com/css2?family=Josefin+Sans:wght@600;700&family=Questrial&display=swap">
<style>
  :root {
    --stage: #666666;
    --paper: #ffffff;
    --ink-dark: #2a2a2c;
    --ink-brand: #4a4a4c;
    --accent-teal: #4fd3dc;
    --bullet: #8c8c8c;
    --text-light: #f2f2f2;
  }
  html, body {
    margin: 0;
    width: 1200px;
    height: 903px;
    overflow: hidden;
    background: var(--stage);
  }
  .banner {
    position: absolute;
    left: 460px;
    top: 31px;
    width: 280px;
    height: 840px;
    display: block;
  }
  .brand-name { font-family: "Questrial", sans-serif; font-size: 21px; fill: var(--ink-brand); letter-spacing: 0.5px; }
  .brand-sub { font-family: "Questrial", sans-serif; font-size: 12px; fill: var(--ink-brand); letter-spacing: 1.5px; }
  .headline { font-family: "Josefin Sans", sans-serif; font-weight: 700; font-size: 14.5px; fill: var(--text-light); }
  .subline { font-family: "Questrial", sans-serif; font-weight: 700; font-size: 11px; fill: var(--accent-teal); }
  .course { font-family: "Questrial", sans-serif; font-size: 10.5px; fill: var(--text-light); }
  .bullet { fill: var(--bullet); }
  .logo-ring { fill: none; stroke: #9a9a9a; stroke-width: 1.5; }
</style>
</head>
<body>
<svg class="banner" viewBox="0 0 310 930" xmlns="http://www.w3.org/2000/svg">
  <defs>
    <linearGradient id="amethyst" x1="0" y1="0" x2="1" y2="1">
      <stop offset="0" stop-color="#5e4a5c"/><stop offset="1" stop-color="#b7aab6"/>
    </linearGradient>
    <linearGradient id="slate" x1="1" y1="0" x2="0" y2="1">
      <stop offset="0" stop-color="#d8d8d8"/><stop offset="1" stop-color="#3a3a3a"/>
    </linearGradient>
    <linearGradient id="steel" x1="0" y1="0" x2="1" y2="1">
      <stop offset="0" stop-color="#cfcfcf"/><stop offset="1" stop-color="#6d6d6d"/>
    </linearGradient>
    <linearGradient id="darkTable" x1="1" y1="0" x2="0" y2="1">
      <stop offset="0" stop-color="#4a4a4a"/><stop offset="1" stop-color="#9a8c84"/>
    </linearGradient>
    <linearGradient id="studio" x1="0" y1="0" x2="0" y2="1">
      <stop offset="0" stop-color="#9a9a9c"/><stop offset="1" stop-color="#2e2c30"/>
    </linearGradient>
    <linearGradient id="workbench" x1="0" y1="0" x2="1" y2="1">
      <stop offset="0" stop-color="#6b5a52"/><stop offset="1" stop-color="#c8b49c"/>
    </linearGradient>
  </defs>

  <rect class="banner-paper" width="310" height="930" fill="var(--paper)"/>

  <!-- brand block -->
  <g class="brand">
    <circle class="logo-ring" cx="157" cy="75" r="33"/>
    <text class="brand-name" x="157" y="140" text-anchor="middle">MIRA HALDEN</text>
    <text class="brand-sub" x="157" y="159" text-anchor="middle">jewellery</text>
  </g>

  <!-- photo tiles -->
  <polygon role="img" aria-label="Photo: gemstone rings resting on amethyst crystal" fill="url(#amethyst)" points="0,84 145,225 0,364"/>
  <polygon role="img" aria-label="Photo: square black-stone ring on dark slate" fill="url(#slate)" points="310,74 168,222 310,364"/>
  <polygon role="img" aria-label="Photo: pavé band ring on a steel mandrel" fill="url(#steel)" points="0,380 148,528 0,676"/>
  <polygon role="img" aria-label="Photo: enamelled leaf pendant and gem rings on a dark table" fill="url(#darkTable)" points="310,380 166,528 310,676"/>
  <polygon role="img" aria-label="Photo: group of students standing in the studio in front of a screen" fill="url(#studio)" points="157,538 303,684 157,808 10,684"/>
  <polygon role="img" aria-label="Photo: student smiling at a jeweller's bench" fill="url(#workbench)" points="0,692 148,840 58,930 0,930"/>
  <polygon role="img" aria-label="Photo: student sawing metal at a workbench" fill="url(#workbench)" points="310,692 166,840 256,930 310,930"/>
  <polygon role="img" aria-label="Photo: ornate gemstone brooch" fill="#b9a9a0" points="157,850 236,930 78,930"/>

  <!-- central message diamond -->
  <polygon class="message-panel" fill="var(--ink-dark)" points="157,227 307,370 157,522 4,370"/>

  <g class="message">
    <text class="headline" x="155" y="287" text-anchor="middle">SO YOU</text>
    <text class="headline" x="155" y="305" text-anchor="middle">WANT TO BE A</text>
    <text class="headline" x="155" y="323" text-anchor="middle">JEWELLERY DESIGNER?</text>

    <text class="subline" x="156" y="349" text-anchor="middle">Part time and full-time classes</text>
    <text class="subline" x="156" y="363" text-anchor="middle">available in:</text>

    <circle class="bullet" cx="42" cy="381" r="3"/>
    <text class="course" x="50" y="384.5">Silversmithing</text>
    <circle class="bullet" cx="132" cy="381" r="3"/>
    <text class="course" x="144" y="384.5">Computer aided design</text>

    <circle class="bullet" cx="70" cy="406" r="3"/>
    <text class="course" x="78" y="409.5">Stone setting</text>
    <circle class="bullet" cx="163" cy="406" r="3"/>
    <text class="course" x="175" y="409.5">Gemmology</text>

    <circle class="bullet" cx="76" cy="431" r="3"/>
    <text class="course" x="85" y="434.5">Jewellery design &amp; rendering</text>

    <circle class="bullet" cx="126" cy="460" r="3"/>
    <text class="course" x="134" y="463.5">Enamelling</text>
  </g>
</svg>
</body>
</html>
```